Meridane Works, Inc. - Update our Website

Meridane Works needs a website to help our customers to navigate through our services efficiently. Our existing website is at www.meridwork.example

We would like to explain our services with content and pictures (photographs) that distinguishes our products and services from our competition.

The website design must implement a strategy to focus on our Contract Labeling services.

With this new design we would like to attract new customers and ensure that our existing customers are fully informed with our latest offerings.

```html
<!DOCTYPE html>
<html lang="en">
<head>
<meta charset="utf-8">
<title>Meridane Works, Inc.</title>
<link rel="stylesheet" href="https://fonts.googleapis.com/css2?family=Barlow:wght@400;500;600;700&display=swap">
<style>
:root{
  --blue:#0a79b8;
  --blue-dark:#0b6ea8;
  --footer:#0b7dbd;
  --green:#7cc70f;
  --text:#1b1b1b;
  --rule:#c9c9c9;
  --white:#ffffff;
}
*{box-sizing:border-box;margin:0;padding:0}
html,body{width:845px;height:1200px;overflow:hidden;background:var(--white)}
body{font-family:"Barlow",sans-serif;color:var(--text)}
.page{position:relative;width:845px;height:1200px;overflow:hidden}
.abs{position:absolute}

/* header */
.site-header{position:absolute;left:0;top:0;width:845px;height:59px;background:var(--white);border-bottom:4px solid var(--green)}
.brand{position:absolute;left:21px;top:17px;display:flex;align-items:center;gap:7px;font-weight:700;font-size:15px;color:#222;letter-spacing:.5px;text-transform:uppercase}
.brand-dot{width:22px;height:22px;border-radius:50%;background:var(--green)}
.main-nav{position:absolute;right:18px;top:28px;display:flex;font-size:10.5px;font-weight:600;color:var(--blue);letter-spacing:.2px}
.main-nav span.sep{margin:0 12px}

/* hero */
.hero{position:absolute;left:0;top:63px;width:845px;height:261px;background:linear-gradient(180deg,#f3f4f5,#fff 40%);border-bottom:4px solid var(--green)}
.hero-photo{position:absolute;left:0;top:0;width:380px;height:257px;background:linear-gradient(90deg,#d9dcdf 0%,#eceef0 55%,#fafafa 100%)}
.hero-title{position:absolute;left:400px;top:67px;font-size:29px;line-height:28px;font-weight:700;color:var(--blue);text-transform:uppercase;letter-spacing:.4px}
.hero-text{position:absolute;left:400px;top:129px;width:380px;font-size:9.6px;line-height:17.6px;font-weight:600;color:#111}
.btn{display:inline-block;background:var(--blue);color:var(--white);font-weight:600;text-transform:uppercase;text-align:center}
.hero-btn{position:absolute;left:401px;top:204px;width:101px;height:30px;line-height:30px;font-size:14px}
.dots{position:absolute;left:613px;top:216px;display:flex;gap:13px}
.dot{width:12px;height:12px;border-radius:50%;border:2px solid var(--blue);background:var(--white)}
.dot.active{background:var(--green);box-shadow:inset 0 0 0 2px var(--white)}

/* welcome */
.welcome-title{position:absolute;left:0;top:356px;width:845px;text-align:center;font-size:28px;line-height:29px;font-weight:700;color:var(--blue);text-transform:uppercase}
.welcome-text{position:absolute;left:40px;top:420px;width:765px;text-align:center;font-size:10px;line-height:11px}
.welcome-btn{position:absolute;left:384px;top:450px;width:77px;height:23px;line-height:23px;font-size:10.5px}

/* feature */
.feature-title{position:absolute;left:33px;top:476px;font-size:20px;font-weight:700;color:var(--blue)}
.feature-sub{position:absolute;left:33px;top:499px;width:476px;display:flex;align-items:center;font-size:13.5px;font-weight:600;color:var(--blue);text-transform:uppercase}
.feature-sub::after{content:"";flex:1;height:1px;background:var(--rule);margin-left:3px}
.feature-text{position:absolute;left:35px;top:525px;width:478px;font-size:9.6px;line-height:14.2px}
.feature-rule{position:absolute;left:33px;top:637px;width:476px;height:1px;background:var(--rule)}
.feature-photo{position:absolute;left:528px;top:508px;width:282px;height:129px;border:1px solid #d0d0d0;background:linear-gradient(135deg,#6d7378 0%,#b9bcbf 40%,#e6e6e4 70%,#c9ccce 100%)}

/* cards */
.card-bar{position:absolute;top:683px;height:5px;width:254px;background:var(--blue)}
.card{position:absolute;top:700px;width:253px;height:248px;border:2px solid #dcdcdc;background:var(--white)}
.card-photo{height:102px}
.card-label{height:27px;line-height:28px;background:var(--green);color:var(--white);font-weight:600;font-size:13px;padding-left:19px;text-transform:uppercase}
.card-text{padding:16px 0 0 20px;width:225px;font-size:9.5px;line-height:10.5px}
.card-btn{position:absolute;right:20px;bottom:11px;width:95px;height:22px;line-height:22px;font-size:10.5px}

/* footer */
.site-footer{position:absolute;left:0;top:980px;width:845px;height:220px;background:var(--footer);color:var(--white)}
.f-head{position:absolute;top:48px;font-size:18px;font-weight:600;text-transform:uppercase;letter-spacing:.3px}
.f-text{position:absolute;font-size:10px;line-height:17.6px;font-weight:500}
.f-divider{position:absolute;top:32px;width:1px;height:172px;background:#0a5f91}
.phone-row{display:flex}
.phone-row b{font-weight:500;width:61px}
.socials{position:absolute;left:405px;top:180px;display:flex;gap:14px}
.social{width:20px;height:20px;border-radius:50%;border:2px solid var(--white);background:var(--footer)}
.subscribe{position:absolute;left:634px;top:124px;display:flex;border:1px solid #0a5f91}
.subscribe .field{width:111px;height:27px;background:var(--white);color:#7a8a95;font-size:9.5px;line-height:27px;padding-left:7px;letter-spacing:.4px;border:1px solid var(--white)}
.subscribe .submit{width:60px;height:27px;line-height:27px;text-align:center;font-size:10px;font-weight:600;background:var(--footer);border-left:1px solid #0a5f91}
</style>
</head>
<body>
<div class="page">

  <header class="site-header">
    <div class="brand"><span class="brand-dot"></span>Meridane Works, Inc.</div>
    <nav class="main-nav">
      <span>HOME</span><span class="sep">|</span>
      <span>ABOUT US</span><span class="sep">|</span>
      <span>OUR SERVICES</span><span class="sep">|</span>
      <span>OUR PRODUCTS</span><span class="sep">|</span>
      <span>USER SUPPORT</span><span class="sep">|</span>
      <span>CONTACT YS</span>
    </nav>
  </header>

  <section class="hero">
    <div class="hero-photo" role="img" aria-label="Photograph of a smiling doctor in a white coat with a stethoscope in a bright office"></div>
    <h1 class="hero-title">With clinical label stock<br>my job has become easier!</h1>
    <p class="hero-text">MeriStock™ is a premium line of label stock products that Meridane Works supplies to the pharmaceutical industry. These label STOCKS are specifically designed for use by clinical supply departments for the computer printing of clinical study labels.</p>
    <span class="btn hero-btn">Read More</span>
    <div class="dots"><span class="dot active"></span><span class="dot"></span><span class="dot"></span></div>
  </section>

  <h2 class="welcome-title">Welcome to<br>Meridane Works, Inc offical website</h2>
  <p class="welcome-text">Meridane Works, Inc. SPECIALIZES in providing products and services to the pharmaceutical industry. We are focused on the needs of those individuals involved with Clinical Trial Materials. Our products and services are summarized below, to know more about our company</p>
  <span class="btn welcome-btn">Read More</span>

  <h3 class="feature-title">MERISTOCK™</h3>
  <div class="feature-sub">Clinical Label Stock</div>
  <p class="feature-text">MeriStock™ is a premium line of label stock products that Meridane Works supplies to the pharmaceutical industry. These label STOCKS are specifically designed for use by clinical supply departments for the computer printing of clinical study labels. Labels are available from our in-house inventories or converted for you on a custom basis. This allows you to obtain the correct combination of size and structural configuration with the appropriate facesheet, ink, adhesive and liner material for your REQUIREMENTS. Labels can be finished in fanfolds, rolls or sheets for use with a wide variety of computer printer technologies.</p>
  <div class="feature-rule"></div>
  <div class="feature-photo" role="img" aria-label="Photograph of gloved hands handling a label roll beside a label printer and keyboard"></div>

  <div class="card-bar" style="left:30px"></div>
  <div class="card-bar" style="left:297px"></div>
  <div class="card-bar" style="left:563px"></div>

  <article class="card" style="left:31px">
    <div class="card-photo" role="img" aria-label="Photograph of hands filling in a printed clinical form next to sample vials" style="background:linear-gradient(135deg,#e9ecee,#cfd4d8 60%,#f4f4f4)"></div>
    <div class="card-label">MeriServ™</div>
    <p class="card-text">MeriServ™ is a contract clinical label generation service that provides you with ready to APPLY clinical labels specifically designed and produced for your clinical trial needs.</p>
    <span class="btn card-btn">Read More</span>
  </article>

  <article class="card" style="left:296px">
    <div class="card-photo" role="img" aria-label="Photograph of a lab technician in blue gloves handling test tubes on a laboratory bench" style="background:linear-gradient(135deg,#8fc9c2,#d9e6ea 50%,#7fa3c4)"></div>
    <div class="card-label">MeriBook™</div>
    <p class="card-text">MeriServ™ is a contract clinical label generation service that provides you with ready to APPLY clinical labels specifically designed and produced for your clinical trial needs.</p>
    <span class="btn card-btn">Read More</span>
  </article>

  <article class="card" style="left:564px">
    <div class="card-photo" role="img" aria-label="Photograph of a doctor in a white coat standing in a bright office" style="background:linear-gradient(90deg,#dadde0,#eef0f1 60%,#f8f8f8)"></div>
    <div class="card-label">Clinical Randomizations</div>
    <p class="card-text">MeriServ™ is a contract clinical label generation service that provides you with ready to APPLY clinical labels specifically designed and produced for your clinical trial needs.</p>
    <span class="btn card-btn">Read More</span>
  </article>

  <footer class="site-footer">
    <h4 class="f-head" style="left:34px">Offices and Locations</h4>
    <div class="f-text" style="left:34px;top:71px;width:160px">
      214 LARCHMONT ROAD<br>ASHFORD HOLLOW<br>NY 11590-2218 USA
      <div class="phone-row"><b>PHONE:</b>+1-555-310-4420</div>
      <div class="phone-row"><b>FAX:</b>+1-555-310-4471</div>
    </div>
    <div class="f-text" style="left:203px;top:71px;width:170px">
      88 MILLBROOK LANE<br>KELTON<br>NJ 08610 USA
      <div class="phone-row"><b>PHONE:</b>+1-555-482-0090</div>
      <div class="phone-row"><b>FAX:</b>+1-555-482-0135</div>
    </div>
    <div class="f-divider" style="left:373px"></div>

    <h4 class="f-head" style="left:405px">Direct Contact</h4>
    <div class="f-text" style="left:405px;top:71px;width:180px;line-height:14.5px">Lorem ipsuCum sociis natoque penatibus et magnis dis parturient</div>
    <div class="f-text" style="left:405px;top:112px">(555) 0142 883201</div>
    <div class="f-text" style="left:405px;top:141px">hello@meridwork.example</div>
    <div class="socials">
      <span class="social" role="img" aria-label="Social network link"></span>
      <span class="social" role="img" aria-label="Social network link"></span>
      <span class="social" role="img" aria-label="Social network link"></span>
    </div>
    <div class="f-divider" style="left:596px"></div>

    <h4 class="f-head" style="left:634px">Newsletter</h4>
    <div class="f-text" style="left:634px;top:71px;width:190px">Join our mailing list and stay tuned to our latest news.</div>
    <div class="subscribe">
      <span class="field">MAIL@DOMAIN.COM</span>
      <span class="submit">SUBMIT</span>
    </div>
    <div class="f-text" style="left:634px;top:182px">All rights reserved . 2014</div>
  </footer>

</div>
</body>
</html>
```